Church Lanterns Over Millbrook Gospel Booklet Design

We need a booklet designed that we will be printing to hand out in our community. Wording for each page will be provided and we need graphic design to produce the layouts in a format ready for print. Booklet will be 4.75" x 4.75" square and a total of 12 pages: 1 cover page front, 1 cover page back, 10 inside pages some of which will be full spread across 2 pages.

Target Market(s)

English speaking Westerners

Industry/Entity Type

Religious

Font styles to use
Serif

Colors
ffffff
85abd2
0292cd
33b8a4
5c5c5c

Requirements
Must have
• Minimalist design with clean look described in attached document
Nice to have
• Aesthetically pleasing graphics, crisp fonts, excellent turn around times
Should not have
• Effeminate design, busy look with too much graphic and text

```html
<!DOCTYPE html>
<html lang="en">
<head>
<meta charset="UTF-8">
<title>Lanterns Over Millbrook – Gospel Booklet Spread</title>
<link rel="stylesheet" href="https://fonts.googleapis.com/css2?family=Lora:wght@500;700&family=Playfair+Display:wght@500;700&display=swap">
<style>
  :root {
    --paper-white: #ffffff;
    --sky-blue: #85abd2;
    --brand-blue: #0292cd;
    --brand-teal: #33b8a4;
    --ink-grey: #5c5c5c;
    --page-deep: #1e5f7e;
    --sky-pale: #bcd2e8;
    --ridge-teal: #4aa8b4;
    --valley-deep: #136f92;
  }
  * { margin: 0; padding: 0; box-sizing: border-box; }
  html, body {
    width: 1200px;
    height: 600px;
    overflow: hidden;
    background: var(--paper-white);
  }
  .spread {
    display: flex;
    width: 1200px;
    height: 600px;
  }
  .page-message {
    width: 600px;
    height: 600px;
    background: linear-gradient(180deg, var(--page-deep) 0%, #18506b 100%);
    color: var(--paper-white);
    font-family: "Lora", serif;
    font-weight: 500;
    font-size: 21px;
    line-height: 32px;
    text-align: center;
    padding: 112px 92px 0 92px;
  }
  .page-message p + p { margin-top: 32px; }
  .page-message strong { font-weight: 700; color: var(--paper-white); }
  .page-verse {
    position: relative;
    width: 600px;
    height: 600px;
    overflow: hidden;
  }
  .verse-backdrop {
    position: absolute;
    inset: 0;
    background: linear-gradient(180deg,
      var(--sky-pale) 0%,
      var(--sky-blue) 38%,
      #6fb0c6 55%,
      var(--ridge-teal) 70%,
      var(--valley-deep) 88%,
      #0c5674 100%);
  }
  .verse {
    position: absolute;
    inset: 0;
    font-family: "Playfair Display", serif;
    text-transform: uppercase;
    text-align: center;
  }
  .verse span {
    position: absolute;
    left: 0;
    right: 0;
    display: block;
    white-space: nowrap;
  }
  .verse-line {
    color: var(--paper-white);
    font-weight: 500;
    font-size: 15px;
    letter-spacing: 2px;
    line-height: 20px;
  }
  .verse-key {
    color: var(--ink-grey);
    font-weight: 700;
    letter-spacing: 1.6px;
  }
  .line-confess { top: 120px; }
  .verse-key.lord { top: 150px; font-size: 31px; line-height: 44px; }
  .line-believe { top: 215px; }
  .line-raised { top: 248px; }
  .verse-key.saved { top: 280px; font-size: 30px; line-height: 44px; }
  .verse-reference {
    position: absolute;
    left: 0;
    right: 0;
    top: 460px;
    text-align: center;
    font-family: "Playfair Display", serif;
    font-weight: 700;
    font-size: 15px;
    letter-spacing: 2px;
    text-transform: uppercase;
    color: var(--paper-white);
  }
</style>
</head>
<body>
  <main class="spread">
    <section class="page-message">
      <p>Next, God has given us the <strong>Bible</strong> and <strong>his church</strong> as the key tools for us to grow in our understanding of God and our personal relationship with him.</p>
      <p>So, it is essential you find a local church that believes the Bible is 100% true. Tell one of the pastors you are a brand new Christian and they will help you from there.</p>
    </section>
    <section class="page-verse">
      <div class="verse-backdrop" role="img" aria-label="Photograph of layered misty mountain ridges under a soft hazy sky"></div>
      <blockquote class="verse">
        <span class="verse-line line-confess">If you confess with your mouth,</span>
        <span class="verse-key lord">“Jesus is Lord,”</span>
        <span class="verse-line line-believe">And believe in your heart that</span>
        <span class="verse-line line-raised">God raised him from the dead,</span>
        <span class="verse-key saved">You will be saved.</span>
      </blockquote>
      <p class="verse-reference">Romans 10:9</p>
    </section>
  </main>
</body>
</html>
```